VelloTek needs web site design

We need a web site design for our product called 'VelloTek'. We develop an asset management system that can manage all kind of assets. Currently we have a logo theme and would like to use similar color scheme; the content concept is pretty much in http://tdalwynne.net but the product was called "Kestel Suite" at the time and is now called "VelloTek". Vello means Vast Equipment Ledger Logging Organizer.
Please use generic image for asset (not just bridges) e.g buildings, trucks, powerlines. train, bus, lightrail etc..
Please emphazise on the data management and security, and distributed networking.

the new website address is https://www.vellotek.example/

name on business card

Thomas Dalwynne 555-014-7392
Principal Architect / Software Engineer

Tara Dalwynne 555-018-2641
Software Engineer

Coding

Coded - Design and coding required

Number of Pages Required

1 page

```html
<!DOCTYPE html>
<html lang="en">
<head>
<meta charset="utf-8">
<title>VelloTek Asset Management</title>
<link href="https://fonts.googleapis.com/css2?family=Lato:wght@400;700;900&family=Montserrat:wght@400;500;700&display=swap" rel="stylesheet">
<style>
:root{
  --navy:#0d1278;
  --navy-deep:#0a0e6a;
  --gold:#c9a13f;
  --gold-dark:#b88f2e;
  --ink:#222;
  --muted:#666;
  --line:#d9d9d9;
  --grey-bg:#ececec;
  --white:#fff;
}
*{box-sizing:border-box;margin:0;padding:0}
html,body{width:1200px;height:2908px;overflow:hidden}
body{position:relative;font-family:"Lato",sans-serif;color:var(--ink);background:var(--white)}
a{color:inherit;text-decoration:none}

/* header */
.site-header{position:absolute;top:0;left:0;width:1200px;height:122px;background:var(--white)}
.brand{position:absolute;left:120px;top:36px;display:flex;align-items:center;gap:12px}
.brand-square{width:44px;height:44px;background:var(--navy)}
.brand-name{font-family:"Lato",sans-serif;font-weight:900;font-size:36px;color:var(--navy);letter-spacing:.5px}
.header-phone{position:absolute;left:765px;top:24px;font-size:19px;color:var(--ink);display:flex;align-items:center;gap:8px}
.main-nav{position:absolute;left:405px;top:62px;display:flex;align-items:center;gap:0}
.main-nav a{font-size:15px;letter-spacing:.5px;color:#333;padding:0 20px;line-height:38px}
.main-nav a.is-active{background:var(--navy);color:var(--white);border-radius:20px;padding:0 24px;margin-right:6px}

/* hero */
.hero{position:absolute;top:122px;left:0;width:1200px;height:560px;background:linear-gradient(160deg,#6d6a66 0%,#4a4c52 45%,#2d3442 100%)}
.hero-shade{position:absolute;inset:0;background:rgba(0,0,0,.25)}
.hero-title{position:absolute;top:180px;width:100%;text-align:center;color:var(--white);font-family:"Lato",sans-serif;font-weight:700;font-size:42px;letter-spacing:1px}
.hero-sub{position:absolute;top:234px;width:100%;text-align:center;color:var(--white);font-size:23px;letter-spacing:1px}
.btn{display:inline-block;font-weight:700;font-size:15px;letter-spacing:.5px;text-align:center;border-radius:24px}
.btn-gold{background:var(--gold);color:var(--white)}
.btn-navy{background:var(--navy);color:var(--white)}
.hero .btn{position:absolute;left:516px;top:283px;width:175px;height:43px;line-height:43px}
.hero-dots{position:absolute;top:440px;left:548px;display:flex;align-items:center;gap:5px}
.hero-dots .arrow{width:18px;height:18px;border-radius:50%;background:var(--white)}
.hero-dots .dot{width:8px;height:8px;border-radius:50%;background:rgba(255,255,255,.55)}
.hero-dots .dot.is-on{background:var(--white)}

/* services */
.services-bg{position:absolute;top:682px;left:0;width:1200px;height:520px;background:linear-gradient(#e8e8e8 0%,#efefef 45%,#fff 100%)}
.service-card{position:absolute;top:660px;width:233px;height:242px;background:var(--white);box-shadow:0 2px 8px rgba(0,0,0,.15);text-align:center}
.service-icon{position:absolute;left:70px;top:-40px;width:92px;height:92px;border-radius:50%;background:var(--navy);display:flex;align-items:center;justify-content:center}
.service-title{position:absolute;top:70px;left:10px;right:10px;color:var(--navy);font-weight:700;font-size:16px;line-height:20px}
.service-text{position:absolute;top:120px;left:28px;right:28px;color:var(--muted);font-size:13.5px;line-height:21px}
.service-toggle{position:absolute;left:92px;bottom:-14px;width:48px;height:48px;border-radius:50%;background:var(--gold);display:flex;align-items:center;justify-content:center}

/* about */
.about-mark{position:absolute;left:205px;top:1022px;width:315px;height:296px;border:22px solid var(--navy);display:flex;align-items:center;justify-content:center}
.about-mark span{font-weight:900;font-size:48px;color:var(--navy)}
.about-divider{position:absolute;left:575px;top:1020px;width:1px;height:310px;background:#bbb}
.about-title{position:absolute;left:618px;top:1025px;font-family:"Montserrat",sans-serif;font-weight:500;font-size:32px;color:var(--ink)}
.about-text{position:absolute;left:620px;top:1086px;width:430px;font-size:14px;line-height:25px;color:#555}
.about .btn{position:absolute;left:622px;top:1290px;width:182px;height:46px;line-height:46px}

/* features band */
.features{position:absolute;top:1430px;left:0;width:1200px;height:504px;background:linear-gradient(120deg,#0b0f7a 0%,#141a86 38%,#4a4a8a 62%,#c9a13f 100%)}
.features-notch{position:absolute;top:-1px;left:568px}
.feature-card{position:absolute;top:88px;width:307px;height:300px;border:1px solid rgba(255,255,255,.8);background:linear-gradient(160deg,#4b4f5e,#2f3241);color:var(--white);text-align:center}
.feature-card::before{content:"";position:absolute;inset:0;background:rgba(10,12,40,.35)}
.feature-card > *{position:relative}
.feature-title{margin-top:38px;font-family:"Montserrat",sans-serif;font-size:24px;font-weight:500}
.feature-sub{margin-top:4px;font-size:14px;font-weight:700}
.feature-text{margin:30px auto 0;width:250px;font-size:13px;line-height:20.5px}
.feature-card .btn{position:absolute;left:66px;bottom:-22px;width:175px;height:42px;line-height:42px}

/* news */
.news-title{position:absolute;left:124px;top:1988px;font-size:35px;color:var(--navy);font-weight:400}
.news-edge{position:absolute;top:2055px;width:26px;height:384px;border:1px solid var(--line);background:#f4f4f4}
.news-card{position:absolute;top:2062px;width:453px;height:380px;border:1px solid var(--line);background:var(--white);text-align:center}
.news-photo{height:228px}
.news-photo.charts{background:linear-gradient(135deg,#a34b3a,#e0b070 40%,#6d8ab5 70%,#3a4a6e)}
.news-photo.tablet{background:linear-gradient(135deg,#8fb0d4,#e4ecf4 45%,#3b5c8c 80%,#1d2f4e)}
.news-headline{margin-top:18px;color:var(--gold);font-size:21px;font-weight:700}
.news-text{margin:12px auto 0;width:400px;font-size:13.5px;line-height:20px;color:#444}
.news-more{display:inline-block;margin-top:16px;font-size:13px;font-weight:700;color:var(--navy)}
.news-arrow{position:absolute;top:2222px}

/* footer */
.site-footer{position:absolute;top:2508px;left:0;width:1200px;height:342px;background:var(--navy-deep);color:var(--white)}
.footer-col{position:absolute;top:76px}
.footer-col h3{font-size:20px;font-weight:700;letter-spacing:.3px;margin-bottom:26px}
.footer-col li{list-style:none;font-size:15px;line-height:33px;color:#e8e8f4}
.contact-line{display:flex;gap:14px;font-size:15px;line-height:23px;margin-bottom:16px;color:#e8e8f4}
.social{display:flex;gap:30px;margin-top:4px}
.social span{width:22px;height:22px;border-radius:50%;background:var(--white)}
.footer-bar{position:absolute;top:2850px;left:0;width:1200px;height:58px;background:var(--gold);color:var(--white);font-size:12px;text-align:center;line-height:58px}
</style>
</head>
<body>

<header class="site-header">
  <div class="brand"><span class="brand-square"></span><span class="brand-name">VelloTek</span></div>
  <div class="header-phone">
    <svg width="18" height="18" viewBox="0 0 24 24"><path fill="#c9a13f" d="M6.6 10.8a15 15 0 006.6 6.6l2.2-2.2c.3-.3.7-.4 1-.2 1.1.4 2.3.6 3.6.6.6 0 1 .4 1 1V20c0 .6-.4 1-1 1A17 17 0 013 4c0-.6.4-1 1-1h3.5c.6 0 1 .4 1 1 0 1.3.2 2.5.6 3.6.1.3 0 .7-.2 1z"/></svg>
    555-014-7392 / 555-018-2641
  </div>
  <nav class="main-nav">
    <a class="is-active" href="#">HOME</a><a href="#">ABOUT US</a><a href="#">SERVICES</a><a href="#">PORTFOLIO</a><a href="#">DOWNLOAD</a><a href="#">CONTACT</a>
  </nav>
</header>

<section class="hero" role="img" aria-label="Hands working on a laptop and calculator over financial reports">
  <div class="hero-shade"></div>
  <h1 class="hero-title">ASSET MANAGEMENT SYSTEM</h1>
  <p class="hero-sub">FUSCE TELLUS SED METUS AUGUE CONVALLIS</p>
  <a class="btn btn-gold" href="#">LEARN MORE</a>
  <div class="hero-dots"><span class="arrow"></span><span class="dot is-on"></span><span class="dot"></span><span class="dot"></span><span class="dot"></span><span class="arrow"></span></div>
</section>

<div class="services-bg"></div>

<div class="service-card" style="left:116px">
  <div class="service-icon"><svg width="46" height="40" viewBox="0 0 46 40" fill="none" stroke="#fff" stroke-width="2"><rect x="3" y="3" width="40" height="26" rx="2"/><path d="M17 37h12M23 29v8M18 12l-4 4 4 4M28 12l4 4-4 4M25 10l-4 12"/></svg></div>
  <h2 class="service-title">Software<br>Development</h2>
  <p class="service-text">Aptent taciti sociosqu ad litora torquent per conubia nostra per inceptos</p>
  <div class="service-toggle"><svg width="20" height="12" viewBox="0 0 20 12"><path d="M2 2l8 8 8-8" fill="none" stroke="#fff" stroke-width="3"/></svg></div>
</div>
<div class="service-card" style="left:362px">
  <div class="service-icon"><svg width="46" height="46" viewBox="0 0 46 46" fill="none" stroke="#fff" stroke-width="2"><circle cx="23" cy="23" r="19"/><ellipse cx="23" cy="23" rx="8" ry="19"/><path d="M4 23h38M7 13h32M7 33h32M23 4v38"/></svg></div>
  <h2 class="service-title">Web &amp; Network Based<br>Information System</h2>
  <p class="service-text">Aptent taciti sociosqu ad litora torquent per conubia nostra per inceptos</p>
  <div class="service-toggle"><svg width="20" height="12" viewBox="0 0 20 12"><path d="M2 2l8 8 8-8" fill="none" stroke="#fff" stroke-width="3"/></svg></div>
</div>
<div class="service-card" style="left:608px">
  <div class="service-icon"><svg width="46" height="46" viewBox="0 0 46 46" fill="none" stroke="#fff" stroke-width="2"><circle cx="23" cy="20" r="7"/><circle cx="23" cy="20" r="2.5"/><path d="M23 9v4M23 27v4M12 20h4M30 20h4M15 12l3 3M31 28l-3-3M31 12l-3 3M15 28l3-3M16 42v-6h14v6"/></svg></div>
  <h2 class="service-title">Software Project<br>Management</h2>
  <p class="service-text">Aptent taciti sociosqu ad litora torquent per conubia nostra per inceptos</p>
  <div class="service-toggle"><svg width="20" height="12" viewBox="0 0 20 12"><path d="M2 2l8 8 8-8" fill="none" stroke="#fff" stroke-width="3"/></svg></div>
</div>
<div class="service-card" style="left:855px">
  <div class="service-icon"><svg width="40" height="46" viewBox="0 0 40 46" fill="none" stroke="#fff" stroke-width="2"><path d="M20 3a14 14 0 00-8 25.5V34h16v-5.5A14 14 0 0020 3z"/><path d="M14 38h12M16 42h8M20 10v18M14 16l6 4 6-4"/></svg></div>
  <h2 class="service-title">Computing<br>Consultant</h2>
  <p class="service-text">Aptent taciti sociosqu ad litora torquent per conubia nostra per inceptos</p>
  <div class="service-toggle"><svg width="20" height="12" viewBox="0 0 20 12"><path d="M2 2l8 8 8-8" fill="none" stroke="#fff" stroke-width="3"/></svg></div>
</div>

<section class="about">
  <div class="about-mark"><span>VelloTek</span></div>
  <div class="about-divider"></div>
  <h2 class="about-title">Who We Are</h2>
  <p class="about-text">Dalwynne and Associates is a software development firm since 1989, specializing in structural engineering applications, complex database systems, distributed information systems and web base information systems. Our team of experts has significant experience in a wide range of computing architectures, operating systems, database engines, embedded systems and networking systems. Our goal is to simplify complex computing systems</p>
  <a class="btn btn-navy" href="#">LEARN MORE</a>
</section>

<section class="features">
  <svg class="features-notch" width="64" height="22" viewBox="0 0 64 22"><path d="M0 0h64L32 20z" fill="#fff"/><path d="M24 5l8 7 8-7" fill="none" stroke="#999" stroke-width="2"/></svg>
  <article class="feature-card" style="left:122px" role="img" aria-label="Engineer inspecting infrastructure on site">
    <h3 class="feature-title">Kestel Suite</h3>
    <p class="feature-sub">inspections anywhere and everywhere</p>
    <p class="feature-text">An integrated secure Kestel Inventory Management system that allows inspectors, with minimum training, to work on site at the structure and communicate with all other users connected to the Kestel Suite network</p>
    <a class="btn btn-navy" href="#">LEARN MORE</a>
  </article>
  <article class="feature-card" style="left:452px" role="img" aria-label="Connected devices in a field office">
    <h3 class="feature-title">Works everywhere</h3>
    <p class="feature-sub">occasionally connected smart client</p>
    <p class="feature-text">Occasionally Connected Smart Client application supports both disconnected or connected network capabilities. Users can operate independently of the network and then integrate with the network database once connected to the network.</p>
    <a class="btn btn-navy" href="#">LEARN MORE</a>
  </article>
  <article class="feature-card" style="left:780px" role="img" aria-label="Developer working at a laptop">
    <h3 class="feature-title">Script Extensions</h3>
    <p class="feature-sub">web development</p>
    <p class="feature-text">An integrated secure Kestel Inventory Management system that allows inspectors, with minimum training, to work on site at the structure and communicate with all other users connected to the Kestel Suite network</p>
    <a class="btn btn-navy" href="#">LEARN MORE</a>
  </article>
</section>

<section class="news">
  <h2 class="news-title">Latest News</h2>
  <div class="news-edge" style="left:0;border-left:none"></div>
  <div class="news-edge" style="left:1160px;width:40px;border-right:none"></div>
  <svg class="news-arrow" style="left:44px" width="30" height="60" viewBox="0 0 30 60"><path d="M26 2L4 30l22 28" fill="none" stroke="#555" stroke-width="2"/></svg>
  <svg class="news-arrow" style="left:1118px" width="30" height="60" viewBox="0 0 30 60"><path d="M4 2l22 28L4 58" fill="none" stroke="#555" stroke-width="2"/></svg>
  <article class="news-card" style="left:122px">
    <div class="news-photo charts" role="img" aria-label="Pen pointing at financial charts on a screen"></div>
    <h3 class="news-headline">Curabitur vel mi sit amet magna</h3>
    <p class="news-text">Morbi diam mauris viverra in gravida eu mattis in ante Morbi eget arcu Morbi porta libero id ullamcorper nonummy</p>
    <a class="news-more" href="#">READ MORE &#8250;</a>
  </article>
  <article class="news-card" style="left:602px">
    <div class="news-photo tablet" role="img" aria-label="Hand using a tablet beside a coffee cup"></div>
    <h3 class="news-headline">Curabitur vel mi sit amet magna</h3>
    <p class="news-text">Morbi diam mauris viverra in gravida eu mattis in ante Morbi eget arcu Morbi porta libero id ullamcorper nonummy</p>
    <a class="news-more" href="#">READ MORE &#8250;</a>
  </article>
</section>

<footer class="site-footer">
  <div class="footer-col" style="left:135px">
    <h3>CONTACT US</h3>
    <div class="contact-line"><svg width="16" height="20" viewBox="0 0 16 20"><path fill="#fff" d="M8 0a7 7 0 00-7 7c0 5 7 13 7 13s7-8 7-13a7 7 0 00-7-7zm0 9.5A2.5 2.5 0 118 4.5a2.5 2.5 0 010 5z"/></svg><span>4120 Marlow Ridge Rd, Suite 210<br>Fairhaven, MN 55900 USA</span></div>
    <div class="contact-line"><svg width="18" height="18" viewBox="0 0 24 24"><path fill="none" stroke="#fff" stroke-width="1.6" d="M6.6 10.8a15 15 0 006.6 6.6l2.2-2.2c.3-.3.7-.4 1-.2 1.1.4 2.3.6 3.6.6.6 0 1 .4 1 1V20c0 .6-.4 1-1 1A17 17 0 013 4c0-.6.4-1 1-1h3.5c.6 0 1 .4 1 1 0 1.3.2 2.5.6 3.6.1.3 0 .7-.2 1z"/></svg><span>+1-555-017-4480</span></div>
    <div class="contact-line"><svg width="18" height="14" viewBox="0 0 18 14"><rect x="1" y="1" width="16" height="12" fill="none" stroke="#fff" stroke-width="1.5"/><path d="M1 1l8 7 8-7" fill="none" stroke="#fff" stroke-width="1.5"/></svg><span>info@vellotek.example</span></div>
  </div>
  <div class="footer-col" style="left:490px">
    <h3>COMPANY</h3>
    <ul><li>Home</li><li>About Us</li><li>Services</li><li>Download</li></ul>
  </div>
  <div class="footer-col" style="left:703px">
    <h3>RESOURCES</h3>
    <ul><li>Testimonials</li><li>Blogs</li><li>News</li><li>Conact Us</li></ul>
  </div>
  <div class="footer-col" style="left:922px">
    <h3>FOLLOW US</h3>
    <div class="social"><span></span><span></span><span></span></div>
  </div>
</footer>
<div class="footer-bar">© 2018 Company Name&nbsp; All right reserved&nbsp; Term of Use</div>

</body>
</html>
```